Real Estate Office Front Facade Redesign - ideas needed

Kindly read this brief thoroughly as there are 2 deliverables:
1. Office building façade redesign (see attached logo and also photo of our office building façade)
2. I also require a design for a freestanding signboard that will be coordinated with the design of the office front please see the images attached labelled signboard.

Deliverable number 1:
I am looking for a minimalist contemporary design with strong colours to draw the attention of the passing Traffic.

The office facade is to be repainted so you may choose to recolour the office in any way to coordinate with logo however the attached logo must remain as is. I prefer the colours red black and white or shades of these colours.

Quillon property managers is a new company looking to target property investors in the local area. Most of our clients are from a middle to upper income demographic. We help these investors to rent out their properties and ensure they are maintained in good condition and provide a regular income.

The area we operate in is centrally located and close to the central business district of Perth.

Our office is situated in a residential area on a busy road facing diagonally at 45° down the road. People see our office from their cars whilst driving to work, there is no pedestrian traffic in the area. Therefore the office façade needs to stand out and any signage must be read by quickly passing traffic or convey our brand in seconds. Whilst the view of the office from the road is obscured somewhat by trees from a distance, once within 50 to 100 m of the office the full face of the office front is visible facing directly at the driver.

No measurements are provided for the façade of the office (please see the photo provided), this is a blank canvas as the whole building will be repainted to fit in with YOUR design. A logo is also attached. The colours red black and white are preferred.

Please provide an image of the office with signage/colours superimposed.

Deliverable number 2:
Also attached is an image of a freestanding sign for which I require a design. This sign is used for advertising properties for lease or sale which will be erected outside the front of residential houses. Again this sign needs to be bold and bright with a contemporary design. It needs to stand out from the crowd of many other signs in the area, whilst the sign advertises the property it must also promote our company brand by having a prominent logo. The size of these signboards will either be 1250 mm x 900 mm or 1800 mm x 625 mm. Please note that this sign must be rectangular in shape and cannot have any text or logo protruding outside of the lines of the rectangular sign due to cost restrictions.

Target Market(s)

Industry/Entity Type

Real Estate

Font styles to use
Sans Serif

Colors
ec1f27
ffffff
000000

Requirements
Must have
• Contemporary uncluttered design using the colours red black and white of shades of.
Nice to have
• A prominent logo with the words "Property Managers" easily read by passing traffic.
• Files provided with editable text and the name of the font used.
Should not have
• designs protruding outside of the overall building facia or sign rectangle.

```html
<!DOCTYPE html>
<html lang="en">
<head>
<meta charset="utf-8">
<title>Quillon Property Managers – For Lease Sign</title>
<link rel="stylesheet" href="https://fonts.googleapis.com/css2?family=Lato:wght@300;400;700;900&family=Josefin+Sans:wght@300;400&display=swap">
<style>
  :root {
    --brand-red: #ec1f27;
    --deep-red: #c8060f;
    --bright-red: #ff2230;
    --ink: #000000;
    --paper: #ffffff;
    --backdrop: #e2e3e5;
  }
  html, body {
    margin: 0;
    padding: 0;
    width: 1200px;
    height: 1110px;
    overflow: hidden;
    background: var(--backdrop);
  }
  .lease-sign {
    position: absolute;
    left: 304px;
    top: 157px;
    width: 603px;
    height: 805px;
    display: block;
  }
  .brand-name {
    font-family: "Josefin Sans", "Lato", sans-serif;
    font-weight: 300;
    fill: var(--paper);
  }
  .brand-tagline {
    font-family: "Josefin Sans", "Lato", sans-serif;
    font-weight: 400;
    fill: var(--paper);
  }
  .headline-for {
    font-family: "Lato", sans-serif;
    font-weight: 400;
    fill: var(--paper);
  }
  .headline-lease {
    font-family: "Lato", sans-serif;
    font-weight: 900;
    fill: var(--paper);
  }
  .phone-number {
    font-family: "Lato", sans-serif;
    font-weight: 700;
    fill: var(--paper);
  }
  .phone-label {
    font-family: "Lato", sans-serif;
    font-weight: 700;
    fill: var(--paper);
  }
  .web-address {
    font-family: "Lato", sans-serif;
    font-weight: 700;
    fill: var(--paper);
  }
  .contact-icon { fill: var(--brand-red); }
</style>
</head>
<body>
<svg class="lease-sign" viewBox="0 0 603 805" xmlns="http://www.w3.org/2000/svg" role="img" aria-label="Quillon Property Managers for lease sign">
  <defs>
    <linearGradient id="red-panel" x1="0" y1="0" x2="1" y2="0">
      <stop offset="0" stop-color="var(--deep-red)"/>
      <stop offset="0.5" stop-color="var(--bright-red)"/>
      <stop offset="1" stop-color="var(--deep-red)"/>
    </linearGradient>
    <radialGradient id="lease-glow" cx="0.5" cy="0.5" r="0.6">
      <stop offset="0" stop-color="#f0343c"/>
      <stop offset="1" stop-color="#e81e28"/>
    </radialGradient>
  </defs>

  <!-- sign base -->
  <rect class="sign-base" x="0" y="0" width="603" height="805" fill="var(--ink)"/>

  <!-- brand block -->
  <g class="brand-block">
    <rect class="brand-square" x="267" y="44" width="64" height="64" fill="var(--brand-red)"/>
    <text class="brand-name" x="301" y="176" font-size="47" letter-spacing="4" text-anchor="middle">QUILLON</text>
    <text class="brand-tagline" x="301" y="200" font-size="12.5" letter-spacing="2" text-anchor="middle">PROPERTY MANAGERS</text>
  </g>

  <!-- roof bands -->
  <polygon class="roof-stripe" points="0,283 294,223 603,303 603,313 294,244 0,315" fill="var(--paper)"/>
  <polygon class="roof-panel" points="0,326 294,250 603,320 603,566 0,566" fill="url(#red-panel)"/>

  <!-- headline -->
  <text class="headline-for" x="300" y="363" font-size="92" text-anchor="middle">FOR</text>
  <rect class="lease-frame" x="83" y="387" width="436" height="142" fill="url(#lease-glow)" stroke="var(--paper)" stroke-width="2.5"/>
  <text class="headline-lease" x="301" y="512" font-size="142" text-anchor="middle" textLength="404" lengthAdjust="spacingAndGlyphs">LEASE</text>

  <!-- base stripe -->
  <polygon class="base-stripe" points="0,578 603,571 603,574 0,613" fill="var(--paper)"/>

  <!-- contact details -->
  <g class="contact-mobile">
    <path class="contact-icon" d="M124,633 c-3,1 -5,4 -5,8 c0,9 5,20 13,25 c3,2 6,2 8,0 l2,-2 l-5,-6 l-3,2 c-3,-2 -6,-9 -6,-14 l3,-1 l-2,-8 z"/>
    <text x="146" y="658"><tspan class="phone-number" font-size="35">0400 318 206</tspan><tspan class="phone-label" font-size="24" dx="6">(Mobile)</tspan></text>
  </g>
  <g class="contact-office">
    <path class="contact-icon" fill-rule="evenodd" d="M125,688 h2 v6 h7 a3,3 0 0 1 3,3 v22 a3,3 0 0 1 -3,3 h-10 a3,3 0 0 1 -3,-3 v-22 a3,3 0 0 1 3,-3 h1 z M124,698 v7 h10 v-7 z M124,708 v2 h2 v-2 z M128,708 v2 h2 v-2 z M132,708 v2 h2 v-2 z M124,712 v2 h2 v-2 z M128,712 v2 h2 v-2 z M132,712 v2 h2 v-2 z M124,716 v2 h2 v-2 z M128,716 v2 h2 v-2 z M132,716 v2 h2 v-2 z"/>
    <text x="146" y="716"><tspan class="phone-number" font-size="47">9412 7730</tspan><tspan class="phone-label" font-size="25" dx="8">(Office)</tspan></text>
  </g>

  <!-- web footer -->
  <rect class="web-bar" x="0" y="748" width="603" height="57" fill="url(#red-panel)"/>
  <text class="web-address" x="301" y="783" font-size="23" letter-spacing="4.2" text-anchor="middle">www.quillonproperty.com.au</text>
</svg>
</body>
</html>
```